Marketing Graphics for App

We need a feature graphic to be used in an app store listing for the app Tidewell Puzzler Pro. Tidewell Puzzler Pro is a brain training app that allows people to practice various cognitive skills. Our immediate need is for a graphic that can be scaled to run on the Corvane Appshelf free app of the day promotion. This ad will show up on the lock screen on the Lumora Slate that users will see when the Lumora Slate is turned on before it is unlocked.

We need a layered PSD file, so that internal elements can be scaled/moved. Please see the guidelines for the graphics ads from Corvane.

Concept style guide: https://media.corvane-example.net/ads/guides/CorvaneCreativeStandards.2013.pdf

Technical style guide: https://media.corvane-example.net/ads/guides/CorvaneSlateAdStyleGuide.pdf

I have included some of our existing graphics assets.

See also the app store listing:
http://www.corvane-example.net/apps/item/Q77TRWLMNB

Target Market(s)

Mobile phone app users.

Industry/Entity Type

Training

Requirements
Must have
• Text: Tidewell Puzzler Pro

Text: Exercise Your Brain
Possibly add: Brain Training Games

```html
<!DOCTYPE html>
<html lang="en">
<head>
<meta charset="utf-8">
<title>Tidewell Puzzler Pro – Lock Screen Feature Graphic</title>
<link rel="stylesheet" href="https://fonts.googleapis.com/css2?family=Lato:wght@700;900&display=swap">
<style>
  :root {
    --canvas-bg: #e9eaec;
    --screen-bg: #ffffff;
    --pattern-blue: #c9d8ec;
    --pattern-gold: #f3e1bd;
    --brand-blue: #0d4a92;
    --brand-gold: #e69500;
    --ink: #111111;
    --control-dark: #2e2e2e;
    --control-mid: #5a5a5a;
    --control-light: #8c8c8c;
    --knob-light: #b9b9b9;
    --knob-dark: #6f6f6f;
    --control-text: #ffffff;
  }

  * { box-sizing: border-box; margin: 0; padding: 0; }

  html, body {
    width: 1200px;
    height: 1200px;
    overflow: hidden;
    background: var(--canvas-bg);
  }

  .canvas {
    position: relative;
    width: 1200px;
    height: 1200px;
  }

  .lock-screen {
    position: absolute;
    left: 207px;
    top: 0;
    width: 785px;
    height: 1200px;
    background: var(--screen-bg);
    overflow: hidden;
    font-family: "Lato", Arial, sans-serif;
  }

  .icon-pattern {
    position: absolute;
    inset: 0;
    background:
      radial-gradient(circle at 30% 40%, var(--pattern-gold) 0%, transparent 70%),
      radial-gradient(circle at 70% 60%, var(--pattern-blue) 0%, transparent 70%),
      var(--screen-bg);
    opacity: 0.35;
  }

  .brand-lockup {
    position: absolute;
    left: 0;
    right: 0;
    top: 286px;
    display: flex;
    flex-direction: column;
    align-items: center;
  }

  .brand-mark {
    width: 300px;
    height: 300px;
    border-radius: 50%;
    background: var(--brand-blue);
  }

  .app-name {
    margin-top: 82px;
    font-weight: 900;
    font-size: 44px;
    line-height: 1;
    color: var(--brand-blue);
    white-space: nowrap;
  }

  .tagline {
    margin-top: 24px;
    font-weight: 900;
    font-size: 17px;
    letter-spacing: 0.5px;
    color: var(--ink);
    text-transform: uppercase;
  }

  .control {
    position: absolute;
    top: 955px;
    height: 107px;
    background: linear-gradient(180deg, var(--control-mid) 0%, var(--control-dark) 55%, var(--control-mid) 100%);
  }

  .control--start {
    left: 0;
    width: 202px;
    border-radius: 0 54px 54px 0;
    display: flex;
    align-items: center;
    padding-left: 42px;
    color: var(--control-text);
    font-weight: 900;
    font-size: 19px;
  }

  .control--unlock {
    right: 0;
    width: 205px;
    border-radius: 54px 0 0 54px;
  }

  .unlock-knob {
    position: absolute;
    left: 17px;
    top: 15px;
    width: 77px;
    height: 77px;
    border-radius: 50%;
    background: radial-gradient(circle at 40% 30%, var(--knob-light) 0%, var(--knob-dark) 100%);
    display: flex;
    align-items: center;
    justify-content: center;
  }
</style>
</head>
<body>
  <main class="canvas">
    <section class="lock-screen">
      <div class="icon-pattern" role="img" aria-label="Faint repeating pattern of small two-tone brain icons in pale gold and blue"></div>

      <div class="brand-lockup">
        <div class="brand-mark"></div>
        <h1 class="app-name">Tidewell Puzzler Pro</h1>
        <p class="tagline">Exercise Your Brain</p>
      </div>

      <div class="control control--start">Start Now</div>

      <div class="control control--unlock">
        <div class="unlock-knob">
          <svg class="lock-icon" width="30" height="36" viewBox="0 0 30 36" aria-hidden="true">
            <path d="M8 16 V10 a7 7 0 0 1 14 0 V16" fill="none" stroke="#ffffff" stroke-width="3.5"/>
            <rect x="4" y="15" width="22" height="18" rx="3" fill="#ffffff"/>
            <circle cx="15" cy="23" r="2.6" fill="#6f6f6f"/>
            <rect x="13.8" y="23" width="2.4" height="5" fill="#6f6f6f"/>
          </svg>
        </div>
      </div>
    </section>
  </main>
</body>
</html>
```